Article/Flyer - Reservation of Rights

We would like an article that we normally produce through illustrator in a pdf format to be placed in a Word format. We have provided a sample article/flyer of our normal distribution style. We would like the outcome to be in WORD format

```html
<!DOCTYPE html>
<html lang="en">
<head>
<meta charset="utf-8">
<title>Marlow &amp; Associates – Reservation of Rights</title>
<link href="https://fonts.googleapis.com/css2?family=Cinzel:wght@500;600&family=Source+Sans+3:wght@400;600&display=swap" rel="stylesheet">
<style>
  :root {
    --backdrop: #555555;
    --maroon: #6b0000;
    --maroon-deep: #5a0000;
    --heading: #7a0a0a;
    --ink: #222222;
    --paper: #ffffff;
    --paper-tint: #f1f1f1;
  }
  * { box-sizing: border-box; margin: 0; padding: 0; }
  html, body { width: 1200px; height: 1200px; overflow: hidden; background: var(--backdrop); }
  body { font-family: "Source Sans 3", "Myriad Pro", sans-serif; color: var(--ink); }

  .flyer {
    position: absolute; left: 194px; top: 30px;
    width: 812px; height: 1140px;
    background: linear-gradient(180deg, var(--paper) 0%, var(--paper-tint) 50%, var(--paper) 100%);
    overflow: hidden;
  }

  .hero { position: relative; height: 483px; }
  .hero-photo {
    position: absolute; inset: 0;
    background:
      linear-gradient(180deg, rgba(107,0,0,0) 55%, rgba(107,0,0,0.85) 82%, var(--maroon) 100%),
      linear-gradient(100deg, #c9c4bd 0%, #8a7f74 22%, #2e3a4d 40%, #3a4758 55%, #b9bec4 75%, #6f7a84 100%);
  }
  .brand-banner { position: absolute; top: 0; right: 0; width: 511px; height: 122px; }
  .brand {
    position: absolute; top: 36px; right: 34px; text-align: right; color: #fff;
  }
  .brand-name { font-size: 42px; font-weight: 400; letter-spacing: 0.5px; line-height: 1; }
  .brand-tagline { font-size: 14px; font-weight: 600; margin-top: 8px; }
  .hero-intro {
    position: absolute; left: 25px; right: 25px; bottom: 14px;
    color: #fff; font-size: 17.5px; line-height: 22px; text-align: justify;
  }

  .article { padding: 8px 25px 0; }
  .article h2 {
    font-family: "Cinzel", "Trajan Pro", serif; font-weight: 600;
    color: var(--heading); font-size: 19px; line-height: 26px; margin: 2px 0 4px;
  }
  .article p {
    font-size: 12.3px; line-height: 15.8px; text-align: justify; margin-bottom: 8px;
  }
  .article p.tight { margin-bottom: 0; }

  .site-band {
    position: absolute; left: 0; right: 0; bottom: 0; height: 31px;
    background: var(--maroon); color: #fff;
    font-size: 17px; letter-spacing: 3.5px; text-align: center; line-height: 31px;
  }
</style>
</head>
<body>
<main class="flyer">
  <header class="hero">
    <div class="hero-photo" role="img" aria-label="Photo of a technician in a yellow hard hat working on the wiring of an outdoor air-conditioning unit"></div>
    <svg class="brand-banner" viewBox="0 0 511 122" aria-hidden="true">
      <polygon points="0,0 511,0 511,122 66,122" fill="#6b0000"/>
      <polyline points="3,0 69,117 511,117" fill="none" stroke="#ffffff" stroke-width="3"/>
    </svg>
    <div class="brand">
      <div class="brand-name">Marlow &amp; Associates</div>
      <div class="brand-tagline">Serving Architects, Engineers and Environmental Consultants</div>
    </div>
    <p class="hero-intro">Reporting a claim or potential claim to your professional liability insurance company will trigger a fair amount of return correspondence that often creates confusion rather than clarity. One document that commonly falls into this category is the Reservation of Rights Letter.</p>
  </header>

  <section class="article">
    <h2>What is the Reservation of Rights Letter</h2>
    <p>The Reservation of Rights Letter is a normal part of the insurance claims process. Its purpose is to provide notification from the insurance company to the policy holder that coverage may not apply. While this often comes as alarming news, the Reservation of Rights Letter should not be mistaken as an outright denial -- it does not automatically mean that coverage is being or will be denied.</p>
    <p>This standard correspondence is routinely sent to comply with state laws and preserve the insurance company’s legal ability to deny some, or all, of the claim pending further investigation while the claim is ongoing and being handled by the insurance company. Failure to send the letter could be considered a waiver of their rights at a later time.</p>
    <p>Because information is vague in the early stages of a claim and often is limited to unsubstantiated allegations and a few facts, the Reservation of Rights Letter protects the insurance company’s interests to later deny coverage in whole or part based on evidence revealed during claims handling.</p>

    <h2>Interpreting the Letter</h2>
    <p class="tight">Most of the time the Reservation of Rights Letter is a generic form letter that states your insurance company is proceeding with handling your claim but reserves the right to deny coverage later on based upon any information that reveals reason to deny.</p>
    <p>Legitimate reasons an insurance company may deny coverage include when the loss occurred in relation to your retroactive date, specific exclusions in the policy language, prior knowledge of the incident, and coverage by another policy, among others.</p>
    <p>If the insurance company believes there may be reason for denial at the time the Reservation of Rights Letter is sent, it will be stated in the letter. For example, if the claim alleges breach of warranty, the letter will state that warranties are specifically excluded by the Policy and it will include the policy language to demonstrate the exclusion.</p>
    <p>Even when specific reasons for potential coverage denial are cited, it is important to note that this is not a final verdict nor does it mean complete lack of coverage. Generally the insurance company is obligated to help you if any of your claims are covered by your insurance policy – there is a duty to defend. In cases such as the scenario above, circumstances of the claim will influence what is covered and what may be subject to exclusion.</p>
    <p>Based on investigative conclusions, the insurance company may not be obligated to pay the damages for certain types or aspects of claims.</p>

    <h2>How to Proceed</h2>
    <p>Although the intent of the Reservation of Rights Letter is to protect the insurance company’s interests, it also alerts the policy holder to the fact that some elements of a claim may not be covered and therefore allows the insured to take steps to protect its potentially uninsured interests.</p>
    <p>However, receiving the Reservation of Rights Letter and even the insurance company’s interpretation of the policy language or law that they believe points toward coverage declination does not mean that you are automatically required to accept a denial of coverage.</p>
    <p>The best thing to do upon receiving the letter is to contact your broker and work closely with them and the insurance company claims handling department to ensure the prompt and fair handling of your claim.</p>
  </section>

  <footer class="site-band">www.marlowassociates.com</footer>
</main>
</body>
</html>
```